Dental Design, very professional and noticable

Tindale Ridge Dental Surgery is based in Pelican Waters. We are a fast growing dental surgery and are looking for some professional business cards to send to patients.
We would like to see a design that is Vertical and uses the colours Soft Blue, Silver, White and Black. Maybe a full blue side with moto and details on back? Any other ideas or colours that you may think will make the card look unique is fine.
We need all details on the card that are listed above

Target Market(s)

Families, Retired, Other Professionals and Businesses

Industry/Entity Type

Dental

Contact Information for Business Card

Tindale Ridge Dental Surgery
Family, Cosmetic, Preventative
Dr. Owen Castrey
Dental Surgeon
BDS (Adel) FAE FADI FICD FPFA
phone: (07)50001846
fax: (07)50002917
email: tindaleridgedental@quillpost.com
http://tindaleridgedental.com/

Logo Text

Logo styles of interest
Abstract Logo
Requirements
Must have
• Vertical, Vibrant but Professional, Rounded Edges, Logo on front and back of card (different colours on each side)
Nice to have
• One side completely blue (not sure what shade) with logo and moto on bottom
Other side white, with blue or different coloured logo with details in black and silver?
Logo should show half circle with 1 end as arrow symbolizing pelican waters canal also a magnifine glass also half circled with 1 end as arrow. Any other ideas are welcome.
Should not have
• A tooth. A smile. Toothbrush or Toothpaste. Cornered edges.

```html
<!DOCTYPE html>
<html lang="en">
<head>
<meta charset="utf-8">
<title>Tindale Ridge Dental Surgery – Business Cards</title>
<link rel="stylesheet" href="https://fonts.googleapis.com/css2?family=Cormorant+Garamond:wght@500&family=PT+Sans&family=PT+Sans+Narrow&display=swap">
<style>
  :root {
    --backdrop: #ecebe8;
    --card-blue: #2b3990;
    --card-white: #ffffff;
    --gold-name: #9a7b2d;
    --gold-tagline: #c79c2a;
    --sky: #29abe2;
    --mark-blue: #1b75bc;
    --silver: #808285;
    --ink: #111111;
    --serif: "Cormorant Garamond", serif;
    --sans: "PT Sans", sans-serif;
    --narrow: "PT Sans Narrow", sans-serif;
  }
  html, body {
    margin: 0;
    width: 1200px;
    height: 1200px;
    overflow: hidden;
    background: var(--backdrop);
  }
  .canvas {
    position: relative;
    width: 1200px;
    height: 1200px;
  }
  .card {
    position: absolute;
    top: 220px;
    width: 460px;
    height: 760px;
    border-radius: 34px;
    box-shadow: 0 8px 24px rgba(0,0,0,0.18);
    box-sizing: border-box;
    padding: 70px 36px 0;
    text-align: center;
  }
  .card--front { left: 110px; background: var(--card-blue); }
  .card--back  { left: 630px; background: var(--card-white); }

  .brand-dot {
    width: 190px;
    height: 190px;
    border-radius: 50%;
    margin: 0 auto 34px;
  }
  .card--front .brand-dot { background: var(--gold-name); }
  .card--back  .brand-dot { background: var(--mark-blue); }

  .practice-name {
    font-family: var(--serif);
    font-weight: 500;
    font-size: 40px;
    line-height: 1.05;
    margin: 0;
  }
  .tagline {
    font-family: var(--serif);
    font-weight: 500;
    font-size: 36px;
    line-height: 1.1;
    margin: 4px 0 0;
  }
  .card--front .practice-name { color: var(--gold-name); }
  .card--front .tagline { color: var(--gold-tagline); }
  .card--back  .practice-name { color: var(--ink); }
  .card--back  .tagline { color: var(--silver); }

  .dentist {
    margin-top: 70px;
    color: var(--sky);
    font-family: var(--serif);
    font-weight: 500;
  }
  .dentist-name { font-size: 38px; margin: 0; }
  .dentist-credentials { font-size: 28px; margin: 8px 0 0; letter-spacing: 1px; }

  .contact {
    text-align: left;
    margin-top: 70px;
    padding-left: 10px;
  }
  .contact-line--voice {
    font-family: var(--sans);
    font-size: 28px;
    color: var(--silver);
    margin: 0;
    line-height: 1.3;
  }
  .contact-line--web {
    font-family: var(--narrow);
    font-size: 28px;
    color: var(--ink);
    margin: 0;
    line-height: 1.25;
  }
  .contact-web { margin-top: 44px; }
</style>
</head>
<body>
  <main class="canvas">
    <section class="card card--front" aria-label="Card front">
      <div class="brand-dot"></div>
      <h1 class="practice-name">Tindale Ridge Dental Surgery</h1>
      <p class="tagline">Family, Cosmetics, Preventive</p>
      <div class="dentist">
        <p class="dentist-name">Dr. Owen Castrey , Dental Surgeon</p>
        <p class="dentist-credentials">DBS (Adel) FAE FADI FICD FFPA</p>
      </div>
    </section>

    <section class="card card--back" aria-label="Card back">
      <div class="brand-dot"></div>
      <h2 class="practice-name">Tindale Ridge Dental Surgery</h2>
      <p class="tagline">Family, Cosmetics, Preventive</p>
      <div class="contact">
        <p class="contact-line--voice">Phone:(07)50001846</p>
        <p class="contact-line--voice">Fax:(07)50002917</p>
        <div class="contact-web">
          <p class="contact-line--web">Email:tindaleridgedental@quillpost.com</p>
          <p class="contact-line--web">http://tindaleridgedental.com</p>
        </div>
      </div>
    </section>
  </main>
</body>
</html>
```